Brochure Design For Beauty Salon

We have an existing brochure for our beauty salon business which has been designed in-house.

We need a designer to refresh the look and feel of the brochure, which is intended for print. The print format will be 210mmx210mm (square, stapled).

We need a design for each and every page of the brochure, including the front and back covers.

We are looking for a fresh modern design, quite close to what we already have, but looking more slick and professional.

The primary colors are white, grey and purple. The final design will communicate luxury, prestige and cleanliness and have a heavy focus on creating the feeling of space within each page.

Target Market(s)

Professional Women, aged 20-45

Industry/Entity Type

Beauty Salon

Font styles to use
Sans Serif
Other font styles liked:
• Helvetica

Requirements
Must have
• The project must be ready for print on square paper 210x210mm

```html
<!DOCTYPE html>
<html lang="en">
<head>
<meta charset="utf-8">
<title>Salon Treatment Brochure – Facials Spread</title>
<link rel="stylesheet" href="https://fonts.googleapis.com/css2?family=Montserrat:wght@400;500;600&display=swap">
<style>
  :root {
    --plum: #5e0f33;
    --plum-light: #8a2a55;
    --ink: #3a3a3a;
    --muted: #8c8c8c;
    --paper: #ffffff;
    --backdrop: #d9d9d9;
    --photo-a: #f3e9e2;
    --photo-b: #d9c3b2;
    --photo-c: #e8d8a8;
  }
  * { box-sizing: border-box; margin: 0; padding: 0; }
  html, body { width: 1200px; height: 801px; overflow: hidden; }
  body {
    background: var(--backdrop);
    font-family: "Montserrat", Helvetica, Arial, sans-serif;
    color: var(--ink);
    position: relative;
  }
  .spread {
    position: absolute;
    left: 60px; top: 130px;
    width: 1080px; height: 540px;
    display: flex;
    box-shadow: 0 10px 30px rgba(0,0,0,0.18);
  }
  .page {
    position: relative;
    width: 540px; height: 540px;
    background: var(--paper);
  }
  .page--left { background: linear-gradient(to right, var(--paper) 88%, #f1f1f1); }
  .page--right { background: linear-gradient(to left, var(--paper) 88%, #f1f1f1); }
  .band {
    position: absolute;
    top: 34px; height: 18px; width: 330px;
    background: linear-gradient(to right, var(--plum), var(--plum-light) 60%, var(--plum));
  }
  .page--left .band { left: 30px; }
  .page--right .band { left: 10px; }

  .section { position: absolute; width: 420px; }
  .signature { left: 60px; top: 70px; }
  .eye-lift { left: 60px; top: 300px; }
  .teenage { left: 50px; top: 70px; }

  .section-title {
    font-size: 17px; font-weight: 600; color: var(--plum);
    padding-bottom: 4px; margin-bottom: 8px;
    position: relative;
  }
  .section-title::after {
    content: ""; position: absolute; left: 0; bottom: 0;
    width: 36px; height: 2px; background: var(--plum);
  }
  .section-intro {
    font-size: 9px; color: var(--muted); line-height: 1.4;
    max-width: 320px; margin-bottom: 10px;
  }

  .treatment {
    display: grid;
    grid-template-columns: 1fr 96px;
    column-gap: 14px;
    align-items: baseline;
    margin-bottom: 10px;
  }
  .treatment-name { font-size: 12px; font-weight: 600; color: var(--ink); grid-column: 1; }
  .treatment-price {
    grid-column: 2; grid-row: 1;
    font-size: 11px; color: var(--muted); text-align: right; white-space: nowrap;
  }
  .treatment-desc {
    grid-column: 1;
    font-size: 9px; color: var(--muted); line-height: 1.4;
  }

  .photo {
    position: absolute; left: 60px; top: 250px; width: 440px; height: 250px;
    background: linear-gradient(120deg, var(--photo-a), var(--photo-b) 70%, var(--photo-c));
  }
</style>
</head>
<body>
  <div class="spread">
    <section class="page page--left">
      <div class="band"></div>
      <div class="section signature">
        <h2 class="section-title">Signature Facials</h2>
        <p class="section-intro">Deep cleansing and ultra hydrating, our signature facials are tailor made for your skin.</p>
        <div class="treatment">
          <h3 class="treatment-name">Focuszone Signature Facial</h3>
          <span class="treatment-price">£35 | 30 mins</span>
          <p class="treatment-desc">We focus on key stages of treatment to get you maximum results in a minimum of time.</p>
        </div>
        <div class="treatment">
          <h3 class="treatment-name">Very Elle Signature Facial</h3>
          <span class="treatment-price">£55 | 60 mins</span>
          <p class="treatment-desc">A bespoke facial customised at every stage.</p>
        </div>
        <div class="treatment">
          <h3 class="treatment-name">Luxury Signature Facial</h3>
          <span class="treatment-price">£85 | 90 mins</span>
          <p class="treatment-desc">Upgrade to the luxury facial and enjoy a deeply hydrating masque and soothing touch therapy</p>
        </div>
      </div>
      <div class="section eye-lift">
        <h2 class="section-title">Eye Lift</h2>
        <div class="treatment">
          <h3 class="treatment-name">Eyelift Focuszone Facial</h3>
          <span class="treatment-price">£35 | 30 mins</span>
          <p class="treatment-desc">This intensive, energising professional treatment focuses on the eye area and delivers benefits including lymph drainage, reduced puffiness, fewer visible fine lines and brighter skin around the eyes</p>
        </div>
        <div class="treatment">
          <h3 class="treatment-name">Eyelift Add-on</h3>
          <span class="treatment-price">£15 | 15 mins</span>
          <p class="treatment-desc">This eye-opening service is to illuminate the eye area and promote an energised, positive appearance while the body is experiencing stress. It delivers quick, visible eye benefits. Add this 15 minute service to your regular facial</p>
        </div>
      </div>
    </section>
    <section class="page page--right">
      <div class="band"></div>
      <div class="section teenage">
        <h2 class="section-title">Teenage Facials</h2>
        <p class="section-intro">Fresh Start from Clearline is a skincare range specialising in teen skin</p>
        <div class="treatment">
          <h3 class="treatment-name">Fresh Start Focuszone Facial</h3>
          <span class="treatment-price">£30 | 30 mins</span>
          <p class="treatment-desc">We focus on key stages of treatment to get you maximum results in a minimum of time.</p>
        </div>
        <div class="treatment">
          <h3 class="treatment-name">Fresh Start Signature Facial</h3>
          <span class="treatment-price">£48 | 60 mins</span>
        </div>
        <div class="treatment">
          <h3 class="treatment-name">Fresh Start Luxury Facial</h3>
          <span class="treatment-price">£75 | 90 mins</span>
        </div>
      </div>
      <div class="photo" role="img" aria-label="Photo of a woman relaxing during a facial treatment with towels and candles"></div>
    </section>
  </div>
</body>
</html>
```